Schnapsbrennerei sucht neue Etiketten
Zielgruppe
Wir sind eine örtliche Schnapsbrennerei, die inzwischen seit ein paar Jahren einen eigenen Kundenstamm aufgebaut hat. Nun werden wir im nächsten Jahr einen neuen Verkaufsraum bauen. Aus diesem Grund wollen wir unsere Etiketten komplett überarbeiten.
Ein neues Logo habe ich bereits designen lassen. Diese finden Sie unten im Dokumententenupload. Wir legen viel Wert auf eine sehr hohe Qualität, welche sich sowohl in unserem Logo als auch den Etiketten Wiederspiegeln soll.
Unsere Kundschaft ist hauptsächlich Ü35 und legt viel Wert auf hochwertige Produkte.
Aufgabenstellung
Eines direkt vorne weg: Da wir unsere komplette Produktpalette neu gestalten wollen würde ich Sie bitten, der Einfachheit halber zuerst nur ein Schnapsetikett (z.B. Zwetschge oder Willi), ein Likör Etikett und ein Etikett für unseren Whiskey zu erstellen.
Darüber hinaus bitte ich Sie auch ein Design für unseren neuen Gin und einen Aquavit, welcher im Herbst auf den Markt kommen soll zu designen. Im Anschluss daran, werde ich in der Zusammenarbeit mit Ihnen die Etiketten optimieren wollen.
Sobald ein 'Grundetikett' entstanden ist, sollen dann auch die anderen Schnäpse und Liköre in dem gleichen Stil erstellt werden. Explizit möchte ich daraufhin weisen, dass sowohl die Whiskeys als auch der Gin und der Aquavit nicht zwangsläufig das gleiche 'Grundetikett' wie der Schnaps und der Likör haben sollen. Ist bei unseren aktuellen Etiketten auch nicht der Fall. Sehen Sie in den Bildern unten.
Wir verkaufen unseren Schnaps und Likör in 3 unterschieldichen Größen 0,2; 0,5 und 1,0 Liter. Wir verwenden für die 0,2 und 0,5 die Flasche Lumbra. Das Etikett der 0,5er Flasche soll in etwa 65x120-130 mm sein. Hier sind wir allerdings variabel.
Dieses entstandene Etikett soll dann auf die anderen Flaschen entsprechend angepasst werden.
Sie finden im Dokumentenupload unsere aktuellen Etiketten und das Logo, welches eingebaut werden soll. Auch ein Etikett von einem örtlichen Weingut, welches mir vom Aufbau und der Unterteilung sehr gut gefällt, werde ich mit anhängen. Allerdings ist dieses Bild sehr unscharf. Wie gesagt es geht hierbei hauptsächlich um die Einteilung mit den oberen und den unteren 'Rahmen'.
Auch unsere Preisliste finden Sie Anhang, wobei diese noch in der Rohform ist und das Obst so nicht verwendet wird, aber hier sind die meisten Produkte drauf.
Das Logo gibt es in verschiedenen Farben. Gerne dürfen Sie für die unterschiedlichen Produkte auch unterschiedliche Farben nutzen.
Was ich mir persönlich g..

```html
<!DOCTYPE html>
<html lang="de">
<head>
<meta charset="utf-8">
<title>Hollmeier's Landbrennerei – Etiketten</title>
<link href="https://fonts.googleapis.com/css2?family=Bodoni+Moda:opsz,wght@6..96,400;6..96,500&family=Oswald:wght@400;500&family=Montserrat:wght@500;600&display=swap" rel="stylesheet">
<style>
  :root{
    --stage:#e7e7e9;
    --band:#333436;
    --band-deep:#2b2c2e;
    --cream:#f1efea;
    --gold:#b8923f;
    --gold-light:#d2ae5c;
    --ink:#2a2a2a;
    --white:#f4f2ec;
  }
  *{box-sizing:border-box;margin:0;padding:0}
  html,body{width:1180px;height:1200px;overflow:hidden;background:var(--stage)}
  .label-row{position:absolute;top:270px;left:40px;display:flex;gap:30px}
  .label{position:relative;width:346px;height:660px;background:var(--cream);overflow:hidden;box-shadow:0 2px 10px rgba(0,0,0,.08)}
  .band-top,.band-bottom{position:absolute;left:0;right:0;background:linear-gradient(180deg,var(--band),var(--band-deep))}
  .band-top{top:0;height:160px}
  .band-bottom{bottom:0;height:140px}
  .gold-frame{position:absolute;inset:14px;border:1.2px solid var(--gold);pointer-events:none}
  .brand{position:absolute;top:72px;left:0;right:0;text-align:center}
  .brand-mark{display:block;width:26px;height:26px;margin:0 auto 10px;border:1.5px solid var(--gold-light);border-radius:50%}
  .brand-name{font-family:"Montserrat",sans-serif;font-weight:600;font-size:15px;letter-spacing:3px;color:var(--white)}
  .brand-sub{font-family:"Montserrat",sans-serif;font-weight:500;font-size:6px;letter-spacing:3px;color:var(--white);margin-top:3px}
  .title{position:absolute;top:186px;left:0;right:0;text-align:center;font-family:"Bodoni Moda",serif;color:var(--gold)}
  .title-main{font-size:38px;font-weight:400;letter-spacing:1px;line-height:1;transform:scaleX(.82)}
  .title-sub{font-family:"Oswald",sans-serif;font-weight:400;font-size:24px;letter-spacing:2px;margin-top:8px}
  .title.liqueur{top:188px}
  .liqueur .title-main{font-size:40px;transform:scaleX(.85)}
  .liqueur .title-line2{font-size:30px;margin-top:6px;transform:scaleX(.85)}
  .fruit{position:absolute;left:73px;top:300px;width:200px;height:160px;border-radius:50%}
  .fruit.plum{background:radial-gradient(circle at 60% 45%,#5a2f4e,#3a1d33 55%,rgba(241,239,234,0) 72%),radial-gradient(circle at 30% 60%,#d9b25e,rgba(241,239,234,0) 45%)}
  .fruit.apple{background:radial-gradient(circle at 45% 50%,#8fc84a,#5f9c2c 50%,rgba(241,239,234,0) 72%)}
  .fruit.peach{background:radial-gradient(circle at 35% 45%,#f4a26a,#e36f43 45%,rgba(241,239,234,0) 70%),radial-gradient(circle at 70% 55%,#f6b04a,rgba(241,239,234,0) 45%)}
  .note{position:absolute;top:462px;left:0;right:0;text-align:center;font-family:"Oswald",sans-serif;font-weight:400;font-size:12px;color:var(--ink);letter-spacing:.2px}
  .barrel{position:absolute;top:484px;left:162px;width:22px;height:20px;border-radius:6px;background:#6b6b6b}
  .specs{position:absolute;top:492px;left:28px;right:28px;display:flex;justify-content:space-between;font-family:"Montserrat",sans-serif;font-weight:600;font-size:11px;letter-spacing:1px;color:var(--ink)}
  .maker{position:absolute;bottom:56px;left:0;right:0;text-align:center;font-family:"Montserrat",sans-serif;font-weight:500;font-size:9px;letter-spacing:1.8px;line-height:13px;color:var(--gold-light);text-transform:uppercase}
  .lot{position:absolute;bottom:30px;left:0;right:0;text-align:center;font-family:"Montserrat",sans-serif;font-weight:600;font-size:8px;letter-spacing:.5px;color:var(--white)}
</style>
</head>
<body>
<main class="label-row">

  <article class="label">
    <div class="band-top"></div>
    <div class="band-bottom"></div>
    <div class="gold-frame"></div>
    <header class="brand">
      <span class="brand-mark"></span>
      <div class="brand-name">HOLLMEIER'S</div>
      <div class="brand-sub">LANDBRENNEREI</div>
    </header>
    <h1 class="title">
      <div class="title-main">HOLLMEIER'S</div>
      <div class="title-sub">ZWETCHGE</div>
    </h1>
    <div class="fruit plum" role="img" aria-label="Illustration: halbierte und ganze Zwetschge mit Blatt"></div>
    <p class="note">HOLLMEIER'S BIRNE IM HOLZFASS GEREIFT</p>
    <div class="barrel" role="img" aria-label="Kleines Holzfass-Symbol"></div>
    <div class="specs"><span>40% vol.</span><span>0,5 l</span></div>
    <address class="maker">Edelbrä &amp; Liköre<br>Konrad Hollmeier<br>Lindenweg 12<br>D.97999 Talheim<br>Tel. 09100 / 4821</address>
    <div class="lot">1.07/06</div>
  </article>

  <article class="label">
    <div class="band-top"></div>
    <div class="band-bottom"></div>
    <div class="gold-frame"></div>
    <header class="brand">
      <span class="brand-mark"></span>
      <div class="brand-name">HOLLMEIER'S</div>
      <div class="brand-sub">LANDBRENNEREI</div>
    </header>
    <h1 class="title">
      <div class="title-main">HOLLMEIER'S</div>
      <div class="title-sub">APFEL</div>
    </h1>
    <div class="fruit apple" role="img" aria-label="Illustration: grüner Apfel mit Blatt und Apfelspalte"></div>
    <p class="note">IM HOLZFASS GEREIFT</p>
    <div class="barrel" role="img" aria-label="Kleines Holzfass-Symbol"></div>
    <div class="specs"><span>40% vol.</span><span>0,5 l</span></div>
    <address class="maker">Edelbrä &amp; Liköre<br>Konrad Hollmeier<br>Lindenweg 12<br>D.97999 Talheim<br>Tel. 09100 / 4821</address>
    <div class="lot">1.07/06</div>
  </article>

  <article class="label">
    <div class="band-top"></div>
    <div class="band-bottom"></div>
    <div class="gold-frame"></div>
    <header class="brand">
      <span class="brand-mark"></span>
      <div class="brand-name">HOLLMEIER'S</div>
      <div class="brand-sub">LANDBRENNEREI</div>
    </header>
    <h1 class="title liqueur">
      <div class="title-main">Weinbergs-</div>
      <div class="title-main title-line2">pfirischlikör</div>
    </h1>
    <div class="fruit peach" role="img" aria-label="Illustration: ganzer und halbierter Pfirsich mit Blättern"></div>
    <div class="specs"><span>40% vol.</span><span>0,5 l</span></div>
    <address class="maker">Edelbrä &amp; Liköre<br>Konrad Hollmeier<br>Lindenweg 12<br>D.97999 Talheim<br>Tel. 09100 / 4821</address>
    <div class="lot">1.07/06</div>
  </article>

</main>
</body>
</html>
```